Hair Salon using organic products looking for AWSOME new menu's!!

We want different and fun incorporating our logo. We would love a folding or tri-folding menu. Any ideas would be welcome we like different. We are an quilmo salon in a little colonial town, but don't like the colonial feel. we would like menu's that would not cost an arm and a leg to print. And we could update as prices and services change without having to re-do the entire design.

Target Market(s)

upper class clients with an interest in using plant based products on their hair and skin

Industry/Entity Type

Hair And Beauty

Requirements
Must have
• Logo, area for contact information and ability to list all salon services
Nice to have
• just a really fun different look to set us aside from other salons. We like to be different

```html
<!DOCTYPE html>
<html lang="en">
<head>
<meta charset="UTF-8">
<title>Lumen Salon – Service Menu</title>
<link rel="stylesheet" href="https://fonts.googleapis.com/css2?family=Cinzel:wght@400;600&family=EB+Garamond:ital,wght@0,500;0,700;1,600&display=swap">
<style>
  :root {
    --backdrop: #e8e8e6;
    --ink: #1e1e1e;
    --ink-soft: #262626;
    --gold: #e2c15a;
    --gold-light: #f4e08c;
    --gold-deep: #b8862a;
    --gold-line: #f3dd84;
    --paper-text: #ffffff;
    --gold-gradient: linear-gradient(120deg, #b07a22 0%, #d8ad45 30%, #f5e38c 55%, #dcb24c 75%, #b47f26 100%);
  }
  * { box-sizing: border-box; margin: 0; padding: 0; }
  html, body { width: 1200px; height: 1200px; overflow: hidden; }
  body {
    background: var(--backdrop);
    position: relative;
    font-family: "EB Garamond", Georgia, serif;
  }

  /* ---------- sheets ---------- */
  .sheet {
    position: absolute;
    left: 200px;
    width: 800px;
    height: 565px;
    background: var(--gold-gradient);
    box-shadow: 0 6px 18px rgba(0,0,0,.18);
    overflow: hidden;
  }
  .sheet--inside { top: 20px; }
  .sheet--outside { top: 615px; }
  .frame-line {
    position: absolute;
    border: 1px solid var(--gold-line);
    pointer-events: none;
  }
  .frame-line--outer { inset: 10px; }
  .frame-line--inner { inset: 16px; }

  .inside-field {
    position: absolute;
    left: 27px; top: 27px; right: 24px; bottom: 29px;
    background: var(--ink);
  }

  /* ---------- brand ---------- */
  .brand {
    position: absolute;
    text-align: center;
    font-family: "Cinzel", "Times New Roman", serif;
    color: var(--gold);
    letter-spacing: 3px;
  }
  .brand-dot {
    display: block;
    margin: 0 auto 8px;
    border: 2px solid currentColor;
    border-radius: 50%;
  }
  .brand--inside { left: 63px; top: 62px; width: 160px; font-size: 15px; }
  .brand--inside .brand-dot { width: 40px; height: 40px; }
  .brand--cover { left: 600px; top: 55px; width: 172px; font-size: 18px; color: #f6e7a6; }
  .brand--cover .brand-dot { width: 56px; height: 56px; }
  .brand--back { left: 340px; top: 488px; width: 120px; font-size: 9px; letter-spacing: 2px; color: #fff6d4; }
  .brand--back .brand-dot { width: 24px; height: 24px; margin-bottom: 6px; }
  .brand--card { position: static; font-size: 7px; letter-spacing: 1.5px; color: var(--gold); }
  .brand--card .brand-dot { width: 16px; height: 16px; margin-bottom: 3px; border-width: 1px; }

  /* ---------- service boxes ---------- */
  .menu-box {
    position: absolute;
    border: 1px solid var(--gold);
  }
  .menu-panel {
    position: absolute;
    background: var(--ink);
  }
  .menu-panel .menu-box { inset: 8px; }
  .box-title {
    position: absolute;
    top: -8px; left: 50%;
    transform: translateX(-50%);
    background: var(--gold);
    color: var(--ink);
    font-family: "Cinzel", "Times New Roman", serif;
    font-weight: 600;
    font-size: 11px;
    letter-spacing: 1px;
    padding: 1px 12px 0;
    white-space: nowrap;
    line-height: 14px;
  }
  .service-list {
    list-style: none;
    padding: 28px 10px 0 10px;
    display: flex;
    flex-direction: column;
    gap: 15px;
  }
  .service-line {
    display: flex;
    align-items: flex-end;
    color: var(--paper-text);
    font-weight: 700;
    font-size: 11px;
    line-height: 13px;
  }
  .service-line::before {
    content: "";
    width: 4px; height: 4px;
    border-radius: 50%;
    background: var(--gold);
    margin: 0 6px 4px 0;
    flex: none;
  }
  .leader {
    flex: 1;
    border-bottom: 1px dotted var(--paper-text);
    margin: 0 2px 3px;
  }
  .price {
    border: 1px solid var(--gold);
    font-size: 9.5px;
    line-height: 11px;
    padding: 0 2px;
    flex: none;
  }
  .price--plain { border: 0; padding: 0; }
  .service-note {
    color: var(--paper-text);
    font-style: italic;
    font-weight: 600;
    font-size: 8.5px;
    line-height: 12px;
    padding: 2px 0 0 32px;
  }

  .box--styling  { left: 46px;  top: 137px; width: 202px; height: 370px; }
  .box--coloring { left: 300px; top: 56px;  width: 202px; height: 194px; }
  .box--waxing   { left: 300px; top: 276px; width: 202px; height: 233px; }
  .box--makeup   { left: 545px; top: 56px;  width: 203px; height: 339px; }

  /* ---------- contact card ---------- */
  .contact-card {
    position: absolute;
    left: 545px; top: 405px; width: 203px; height: 123px;
    border: 1px solid var(--gold);
    padding: 4px;
  }
  .contact-inner {
    border: 1px solid var(--gold);
    height: 100%;
    padding: 6px 8px;
    text-align: center;
  }
  .contact-text {
    color: var(--paper-text);
    font-style: italic;
    font-weight: 600;
    font-size: 7.5px;
    line-height: 9.5px;
    text-align: justify;
    margin: 4px 0 6px;
  }
  .social-row {
    display: flex;
    justify-content: center;
    gap: 6px;
  }
  .social-chip {
    width: 17px; height: 17px;
    border-radius: 4px;
    background: var(--gold);
  }

  /* ---------- outside sheet ---------- */
  .ornament {
    position: absolute;
    border-radius: 50%;
    background: radial-gradient(circle, rgba(255,240,170,.35) 0%, rgba(255,240,170,0) 70%);
  }
  .ornament--top    { left: 330px; top: 40px;  width: 200px; height: 160px; }
  .ornament--right  { left: 500px; top: 220px; width: 300px; height: 300px; }
  .ornament--bottom { left: 30px;  top: 400px; width: 240px; height: 165px; }

  .panel--treatment { left: 34px; top: 36px; width: 227px; height: 398px; }
  .panel--treatment .menu-box { inset: 8px 8px 8px 8px; }
  .panel--treatment .box-title { top: -7px; }

  .panel--tips { left: 308px; top: 167px; width: 199px; height: 227px; }
  .tips-text {
    color: var(--paper-text);
    font-style: italic;
    font-weight: 600;
    font-size: 8.5px;
    line-height: 12.2px;
    text-align: justify;
    padding: 20px 8px 0 14px;
    position: relative;
  }
  .tips-text::before {
    content: "";
    position: absolute;
    left: 6px; top: 24px;
    width: 4px; height: 4px;
    border-radius: 50%;
    background: var(--gold);
  }

  .social-row--cover {
    position: absolute;
    left: 623px; top: 515px;
    gap: 8px;
  }
  .social-row--cover .social-chip { width: 19px; height: 19px; background: #8a5f15; }
</style>
</head>
<body>

<!-- Inside spread -->
<section class="sheet sheet--inside" aria-label="Inside of menu">
  <div class="frame-line frame-line--outer"></div>
  <div class="frame-line frame-line--inner"></div>
  <div class="inside-field"></div>

  <div class="brand brand--inside"><span class="brand-dot"></span>Lumen Salon</div>

  <div class="menu-box box--styling">
    <h2 class="box-title">Hair Styling</h2>
    <ul class="service-list">
      <li><div class="service-line">Bridal Up Style<span class="leader"></span><span class="price">$15</span></div><p class="service-note">Lorem ipsum dolor sit, consectetuer adipiscing.</p></li>
      <li><div class="service-line">Blow Dry<span class="leader"></span><span class="price">$10</span></div><p class="service-note">Lorem ipsum dolo r sit, consectetuer adipiscing</p></li>
      <li><div class="service-line">Up Style<span class="leader"></span><span class="price">$20</span></div><p class="service-note">Lorem ipsum dolor sit, consectetuer adipiscing.</p></li>
      <li><div class="service-line">Night Style<span class="leader"></span><span class="price">$15</span></div><p class="service-note">Lorem ipsum dolor sit, consectetuer adipiscing.</p></li>
      <li><div class="service-line">Super Dry<span class="leader"></span><span class="price">$10</span></div><p class="service-note">Lorem ipsum dolo r sit, consectetuer adipiscing</p></li>
      <li><div class="service-line">Diva Style<span class="leader"></span><span class="price">$20</span></div><p class="service-note">Lorem ipsum dolor sit, consectetuer adipiscing.</p></li>
    </ul>
  </div>

  <div class="menu-box box--coloring">
    <h2 class="box-title">Hair Coloring</h2>
    <ul class="service-list">
      <li><div class="service-line">Single Process Color<span class="leader"></span><span class="price">$15</span></div><p class="service-note">Lorem ipsum dolor sit, consectetuer adipiscing.</p></li>
      <li><div class="service-line">Full Highlight<span class="leader"></span><span class="price">$10</span></div><p class="service-note">Lorem ipsum dolo r sit, consectetuer adipiscing</p></li>
      <li><div class="service-line">Partial Highlight<span class="leader"></span><span class="price">$20</span></div><p class="service-note">Lorem ipsum dolor sit, consectetuer adipiscing.</p></li>
    </ul>
  </div>

  <div class="menu-box box--waxing">
    <h2 class="box-title">Waxing</h2>
    <ul class="service-list">
      <li><div class="service-line">Eyebrow<span class="leader"></span><span class="price">$15</span></div><p class="service-note">Lorem ipsum dolor sit, consectetuer adipiscing.</p></li>
      <li><div class="service-line">Lip<span class="leader"></span><span class="price">$10</span></div><p class="service-note">Lorem ipsum dolo r sit, consectetuer adipiscing</p></li>
      <li><div class="service-line">Chin<span class="leader"></span><span class="price">$20</span></div><p class="service-note">Lorem ipsum dolor sit, consectetuer adipiscing.</p></li>
      <li><div class="service-line">Cheeks<span class="leader"></span><span class="price price--plain">$20</span></div><p class="service-note">Lorem ipsum dolor sit, consectetuer adipiscing.</p></li>
    </ul>
  </div>

  <div class="menu-box box--makeup">
    <h2 class="box-title">Make-Up</h2>
    <ul class="service-list">
      <li><div class="service-line">Application<span class="leader"></span><span class="price">$25</span></div><p class="service-note">Lorem ipsum dolor sit, consectetuer adipiscing.</p></li>
      <li><div class="service-line">Eye Application<span class="leader"></span><span class="price">$10</span></div><p class="service-note">Lorem ipsum dolo r sit, consectetuer adipiscing</p></li>
      <li><div class="service-line">Bridal Make-Up<span class="leader"></span><span class="price">$20</span></div><p class="service-note">Lorem ipsum dolor sit, consectetuer adipiscing.</p></li>
      <li><div class="service-line">Make-Up Consultation<span class="leader"></span><span class="price">$25</span></div><p class="service-note">Lorem ipsum dolor sit, consectetuer adipiscing.</p></li>
      <li><div class="service-line">Individual Lashes<span class="leader"></span><span class="price">$10</span></div><p class="service-note">Lorem ipsum dolo r sit, consectetuer adipiscing</p></li>
      <li><div class="service-line">Nigth Make-Up<span class="leader"></span><span class="price price--plain">$20</span></div><p class="service-note">Lorem ipsum dolor sit, consectetuer adipiscing.</p></li>
    </ul>
  </div>

  <div class="contact-card">
    <div class="contact-inner">
      <div class="brand brand--card"><span class="brand-dot"></span>Lumen Salon</div>
      <p class="contact-text">Lorem ipsum dolor sit amet, consectetuer adipiscing elit, sed diam nonummy nibh euismod tincidunt ut laoreet dolore magna aliquam erat volutpat.</p>
      <div class="social-row" aria-label="Social channels">
        <span class="social-chip"></span><span class="social-chip"></span><span class="social-chip"></span><span class="social-chip"></span>
      </div>
    </div>
  </div>
</section>

<!-- Outside spread -->
<section class="sheet sheet--outside" aria-label="Outside of menu">
  <div class="frame-line frame-line--outer"></div>
  <div class="frame-line frame-line--inner"></div>

  <div class="ornament ornament--top" role="img" aria-label="Faint floral ornament"></div>
  <div class="ornament ornament--right" role="img" aria-label="Large faint floral ornament"></div>
  <div class="ornament ornament--bottom" role="img" aria-label="Faint floral ornament"></div>

  <div class="menu-panel panel--treatment">
    <div class="menu-box">
      <h2 class="box-title">Hair Treatment</h2>
      <ul class="service-list">
        <li><div class="service-line">Hydration<span class="leader"></span><span class="price">$15</span></div><p class="service-note">Lorem ipsum dolor sit, consectetuer adipiscing.</p></li>
        <li><div class="service-line">Mask<span class="leader"></span><span class="price">$10</span></div><p class="service-note">Lorem ipsum dolo r sit, consectetuer adipiscing</p></li>
        <li><div class="service-line">Hair surgery<span class="leader"></span><span class="price">$20</span></div><p class="service-note">Lorem ipsum dolor sit, consectetuer adipiscing.</p></li>
        <li><div class="service-line">Night Style<span class="leader"></span><span class="price">$15</span></div><p class="service-note">Lorem ipsum dolor sit, consectetuer adipiscing.</p></li>
        <li><div class="service-line">Super Dry<span class="leader"></span><span class="price">$10</span></div><p class="service-note">Lorem ipsum dolo r sit, consectetuer adipiscing</p></li>
        <li><div class="service-line">Diva Style<span class="leader"></span><span class="price">$20</span></div><p class="service-note">Lorem ipsum dolor sit, consectetuer adipiscing.</p></li>
      </ul>
    </div>
  </div>

  <div class="menu-panel panel--tips">
    <div class="menu-box">
      <h2 class="box-title">Tips</h2>
      <p class="tips-text">Lorem ipsum dolor sit amet, consectetuer adipiscing elit, sed diam nonummy nibh euismod tincidunt ut laoreet dolore magna aliquam erat volutpat. Ut wisi enim ad minim veniam, quis nostrud exerci tation ullamcorper suscipit lobortis nisl ut aliquip ex ea commodo consequat. Duis autem vel eum iriure dolor in hendrerit in vulputate velit esse molestie consequat, vel illum dolore eu feugiat nulla facilisis at vero eros et accumsan et iusto odio dignissim qui blandit praesent luptatum zzril delenit augue duis dolore te feugait nulla facilisi.</p>
    </div>
  </div>

  <div class="brand brand--cover"><span class="brand-dot"></span>Lumen Salon</div>
  <div class="brand brand--back"><span class="brand-dot"></span>Lumen Salon</div>

  <div class="social-row social-row--cover" aria-label="Social channels">
    <span class="social-chip"></span><span class="social-chip"></span><span class="social-chip"></span><span class="social-chip"></span>
  </div>
</section>

</body>
</html>
```